Car wrap for landscaping/gardening company (in Portuguese)

This is a landscaping company that is fully electric, providing, silent, emissions-free landscaping to the community. I am requesting a wrap for the residential van that will be used for this service.

The key things that the wrap must convey, besides the logo of the company, is:
(1) 100% electric (100% Elétrico)
(2) Silent (Silencioso)
(3) No emissions (Sem Emissões)
I envision three large, round icons with a simple image illustrating each of these concepts, and below each icon the text in Portuguese. The van only has to have the logo and the icons, plus a space for phone number and website which can be a little smaller. Use bold colors, make it modern. Don't make it flowery, that will not distinguish the van.

An additional icon can also be added for Customer Service. So possibly 4 icons, with the 4th one saying "Serviço ao Cliente." I am interested in seeing alternatives with 3 and 4 icons.

Please check out the sample that I sent. I like this wrap because it is simple and very visible. It has a lot of text in the rear though which is difficult to read. I don't want this kind of text. Just the icons and the titles. Make it super clear.

The service is high tech, innovative, and premium. It is not a normal landscaping company. I want to attract high end customers who demand the best, who want landscaping that is silent and clean for the environment.

Target Market(s)

Residential customers with patios, large houses, looking for high tech landscaping service and willing to pay a premium

Industry/Entity Type

Landscaping, Gardening

Font styles to use
Sans Serif

Requirements
Must have
• Please use the logo that I have provided. I also need three icons, well displayed, each one representing an aspect of our service: (1) 100% ELÉTRICO (2) SILENCIOSO (3) SEM EMISSÕES. In Portuguese it means 100% electric, Silent, No emissions. Can be three round icons below the logo, very prominent so that people know what the service is about. Also need a place to put two phone numbers, on the back and on the door, as well as the website.
Nice to have
• The picture that I showed is a good example of a blue car wrap. This can work but has to be in green or brown (landscaping colors). I like it because it is bold and visible, and doesn't have too many decorative features. It is very modern and simple, which is consistent with the theme that I am looking for.
Should not have
• Flowery shapes, too much decoration, curvy lines, excessive text

```html
<!DOCTYPE html>
<html lang="pt">
<head>
<meta charset="utf-8">
<title>Verde Quieto – Electric Van Wrap Design</title>
<link href="https://fonts.googleapis.com/css2?family=Poppins:ital,wght@0,400;0,600;0,700;1,500;1,700&display=swap" rel="stylesheet">
<style>
  :root{
    --bg:#f2f2f2;
    --green:#0a7a22;
    --green-deep:#06681b;
    --white:#ffffff;
    --brown:#8a5232;
  }
  *{margin:0;padding:0;box-sizing:border-box}
  html,body{width:1200px;height:1200px;overflow:hidden;background:var(--bg)}
  body{position:relative;font-family:"Poppins",sans-serif}
  .brand-header{position:absolute;left:42px;top:40px}
  .brand-name{font-size:56px;font-weight:600;color:var(--green);letter-spacing:1px;line-height:1}
  .project-label{
    margin-top:16px;display:inline-block;background:var(--green);color:var(--white);
    font-size:30px;font-style:italic;font-weight:500;padding:4px 22px 6px 18px;
    transform:skewX(-4deg);
  }
  .project-label strong{font-weight:700}
  .wrap-layout{position:absolute;left:0;top:0}
  .icon-label{font-family:"Poppins",sans-serif;font-weight:700;font-size:15px}
  .contact-title{font-family:"Poppins",sans-serif;font-weight:600;font-style:italic;font-size:15px;fill:var(--white)}
  .contact-value{font-family:"Poppins",sans-serif;font-weight:700;font-style:italic;fill:var(--white)}
  .address{font-family:"Poppins",sans-serif;font-weight:600;font-style:italic;font-size:14px;fill:var(--white)}
  .name-vertical{font-family:"Poppins",sans-serif;font-weight:600}
</style>
</head>
<body>

<header class="brand-header">
  <div class="brand-name">VERDE QUIETO</div>
  <div class="project-label">Electric Van Wrap <strong>Design</strong></div>
</header>

<svg class="wrap-layout" width="1200" height="1200" viewBox="0 0 1200 1200" xmlns="http://www.w3.org/2000/svg">
  <defs>
    <symbol id="icon-plug" viewBox="0 0 40 40">
      <circle cx="20" cy="20" r="19" fill="var(--white)"/>
      <rect x="13" y="14" width="14" height="11" rx="3" fill="var(--green)"/>
      <rect x="15" y="8" width="3" height="7" fill="var(--green)"/>
      <rect x="22" y="8" width="3" height="7" fill="var(--green)"/>
      <rect x="18.5" y="24" width="3" height="8" fill="var(--green)"/>
    </symbol>
    <symbol id="icon-silent" viewBox="0 0 40 40">
      <circle cx="20" cy="20" r="19" fill="var(--white)"/>
      <path d="M9 16h5l7-6v20l-7-6H9z" fill="var(--green)"/>
      <path d="M25 16l7 8M32 16l-7 8" stroke="var(--green)" stroke-width="2.5" stroke-linecap="round"/>
    </symbol>
    <symbol id="icon-emission" viewBox="0 0 40 40">
      <circle cx="20" cy="20" r="19" fill="var(--white)"/>
      <text x="19" y="25" text-anchor="middle" font-family="Poppins,sans-serif" font-weight="700" font-size="13" fill="var(--green)">CO₂</text>
      <path d="M10 29L30 11" stroke="var(--green)" stroke-width="2.5" stroke-linecap="round"/>
    </symbol>
    <symbol id="icon-support" viewBox="0 0 40 40">
      <circle cx="20" cy="20" r="19" fill="var(--white)"/>
      <path d="M11 22v-3a9 9 0 0 1 18 0v3" fill="none" stroke="var(--green)" stroke-width="2.5"/>
      <rect x="9" y="20" width="5" height="8" rx="2" fill="var(--green)"/>
      <rect x="26" y="20" width="5" height="8" rx="2" fill="var(--green)"/>
      <path d="M28 28q0 4-6 4" fill="none" stroke="var(--green)" stroke-width="2"/>
    </symbol>
  </defs>

  <g class="rear-panel">
    <rect x="60" y="240" width="480" height="770" rx="40" fill="var(--green)"/>
    <path d="M365 275h140q18 0 16 18l-10 250q-2 20-22 20H345z" fill="var(--white)"/>
    <text class="name-vertical" font-size="92" fill="var(--white)" transform="translate(108 300) rotate(90)">QUIETO</text>
    <text class="name-vertical" font-size="100" fill="var(--white)" transform="translate(200 300) rotate(90)">VERDE</text>

    <use href="#icon-plug" x="305" y="300" width="40" height="40"/>
    <text class="icon-label" x="370" y="327" fill="var(--green)">100% ELÉTRICO</text>
    <use href="#icon-silent" x="305" y="360" width="40" height="40"/>
    <text class="icon-label" x="370" y="387" fill="var(--green)">SILENCIOSO</text>
    <use href="#icon-emission" x="305" y="420" width="40" height="40"/>
    <text class="icon-label" x="370" y="447" fill="var(--green)">SEM EMISSÕES</text>
    <use href="#icon-support" x="305" y="480" width="40" height="40"/>
    <text class="icon-label" x="370" y="498" fill="var(--green)">SERVIÇO AO</text>
    <text class="icon-label" x="370" y="516" fill="var(--green)">CLIENTE</text>

    <text class="contact-title" x="310" y="620">Teléfono</text>
    <text class="contact-value" x="310" y="655" font-size="26">888 8 88 888</text>
    <text class="contact-title" x="310" y="710">Sitio Web</text>
    <text class="contact-value" x="310" y="735" font-size="15">verdequieto.com</text>
    <text class="address" x="310" y="820">(your address here)</text>
    <text class="address" x="310" y="842">(your address here)</text>
  </g>

  <g class="side-panel">
    <rect x="580" y="240" width="570" height="770" rx="30" fill="var(--green)"/>
    <path d="M860 240H1120q30 0 30 30V900C980 880 872 720 860 240z" fill="var(--white)"/>
    <text class="name-vertical" font-size="92" fill="var(--green)" transform="translate(960 275) rotate(90)">VERDE</text>
    <text class="name-vertical" x="955" y="705" font-size="44" fill="var(--green)">QUIETO</text>

    <use href="#icon-plug" x="610" y="300" width="40" height="40"/>
    <text class="icon-label" x="665" y="327" fill="var(--white)">100% ELÉTRICO</text>
    <use href="#icon-silent" x="610" y="360" width="40" height="40"/>
    <text class="icon-label" x="665" y="387" fill="var(--white)">SILENCIOSO</text>
    <use href="#icon-emission" x="610" y="420" width="40" height="40"/>
    <text class="icon-label" x="665" y="447" fill="var(--white)">SEM EMISSÕES</text>
    <use href="#icon-support" x="610" y="480" width="40" height="40"/>
    <text class="icon-label" x="665" y="498" fill="var(--white)">SERVIÇO AO</text>
    <text class="icon-label" x="665" y="516" fill="var(--white)">CLIENTE</text>

    <text class="contact-title" x="612" y="620">Teléfono</text>
    <text class="contact-value" x="612" y="660" font-size="32">888 8 88 8888</text>
    <text class="contact-title" x="612" y="715">Sitio Web</text>
    <text class="contact-value" x="612" y="745" font-size="22">verdequieto.com</text>
    <text class="address" x="612" y="930">(your address here)</text>
    <text class="address" x="612" y="952">(your address here)</text>
  </g>
</svg>

</body>
</html>
```